Stellenanzeige Mechaniker für Baumaschinen
Zielgruppe
Was wir machen: Baumaschinenhandel und Vermietung
Was wir suchen: Vollzeitkräfte in der Werkstatt Service und Verkauf
www.baumaschinen-krosbach.de
www.krosbach-rental.de
Aufgabenstellung
Eyecatcher, die Anzeige soll in diversen Medien gestreut werden.
Ihr Aufgabengebiet
Zuverlässig umsetzen: Sie reparieren Neu- und Gebrauchtmaschinen im Außen- und Innendienst
Sicherheit schaffen: Durchführung von Inspektionen, UVV-Prüfungen und Wartungsarbeiten
Probleme beseitigen: Fehler- und Störungsanalyse
Werte entdecken: Aufarbeitung von Gebraucht- und Mietmaschinen
Kundenzufriedenheit garantieren: Aus- und Umrüsten vom Maschinen mit Zubehör Kundenbetreuung im Servicebereich sowie Ersatzteilbeschaffung und Garantieabwicklungen
Ihr Profil
Ausbildung: als Land-/Baumaschinenmechaniker oder vergleichbare Ausbildung
Persönlichkeit: kommunikatives und sympathisches Auftreten, hohes Qualitätsbewusstsein,
Arbeitsweise: selbständig, strukturiert, belastbar und zuverlässig
Erfahrungen und Knowhow: Einschlägige Berufserfahrung in der Branche, Sichere PC-Anwendung (Diagnose-Tools), Gute Kenntnisse in Hydraulik, Elektrik und Motoren
Mobilität: Führerschein Klasse B (Pkw)
Wir bieten:
Zukunfts- und krisensicherer Arbeitsplatz
Interessante und abwechslungsreiche Aufgaben in einer vertrauensvollen Arbeitsatmosphäre
Attraktive Vergütung
Fundierte und strukturierte Einarbeitung
Weiterbildungs- und Entwicklungsmöglichkeiten
Gutes Betriebsklima in einer familiären Atmosphäre
Kurze Entscheidungswege

```html
<!DOCTYPE html>
<html lang="de">
<head>
<meta charset="utf-8">
<title>Stellenanzeige – Krosbach Baumaschinen</title>
<link rel="stylesheet" href="https://fonts.googleapis.com/css2?family=Archivo:wdth,wght@125,800;125,900&family=Barlow+Semi+Condensed:wght@300;400&display=swap">
<style>
  :root {
    --ink: #0b0b0b;
    --paper: #ffffff;
    --teal: #3fc3c9;
    --haze: #c9c3cc;
    --dust: #9c95a3;
  }
  * { box-sizing: border-box; margin: 0; padding: 0; }
  html, body { width: 848px; height: 1200px; overflow: hidden; background: var(--paper); }
  .ad {
    position: relative;
    width: 848px;
    height: 1200px;
    overflow: hidden;
    background: var(--paper);
    color: var(--ink);
    font-family: "Barlow Semi Condensed", "Arial Narrow", sans-serif;
    font-weight: 300;
  }
  .hero {
    position: absolute;
    left: 0; top: 0;
    width: 848px; height: 298px;
    overflow: hidden;
  }
  .hero-photo {
    position: absolute; inset: 0;
    background:
      radial-gradient(ellipse 320px 170px at 620px 110px, rgba(63,195,201,0.85), rgba(63,195,201,0) 75%),
      radial-gradient(ellipse 200px 120px at 120px 220px, rgba(190,215,225,0.9), rgba(190,215,225,0) 80%),
      linear-gradient(180deg, #d7d3d8 0%, var(--haze) 55%, var(--dust) 100%);
  }
  .brand-name {
    position: absolute;
    left: 26px; top: 22px;
    font-family: "Barlow Semi Condensed", "Arial Narrow", sans-serif;
    font-weight: 400;
    font-size: 28px;
    line-height: 30px;
    letter-spacing: 2px;
    color: var(--ink);
  }
  .hero-title {
    position: absolute;
    left: 0; width: 768px;
    top: 151px;
    text-align: center;
    font-family: "Archivo", "Arial Black", sans-serif;
    font-stretch: 125%;
    font-weight: 900;
    font-size: 72px;
    line-height: 76px;
    letter-spacing: -1px;
    color: var(--ink);
    transform: scaleX(1.3);
  }
  .position {
    position: absolute;
    left: 0; right: 0;
    top: 347px;
    text-align: center;
    font-family: "Archivo", "Arial Black", sans-serif;
    font-stretch: 125%;
    font-weight: 800;
    font-size: 24px;
    line-height: 22px;
    letter-spacing: 1.5px;
    transform: scaleX(1.3);
  }
  .details {
    position: absolute;
    left: 42px;
    top: 422px;
    width: 660px;
    font-size: 20px;
    line-height: 24.6px;
  }
  .section-title { font-weight: 300; font-size: 20px; margin-bottom: 2px; }
  .section + .section { margin-top: 25px; }
  .section ul { list-style: none; padding-left: 30px; width: 648px; }
  .section li { position: relative; }
  .section li::before {
    content: "";
    position: absolute;
    left: -12px; top: 12px;
    width: 4px; height: 4px;
    border-radius: 50%;
    background: var(--ink);
  }
  .section li.small { font-size: 17px; margin-left: -3px; }
</style>
</head>
<body>
<main class="ad">
  <header class="hero">
    <div class="hero-photo" role="img" aria-label="Foto: Mechaniker mit Warnweste und Helm an einem türkisfarbenen Kettenbagger, links ein Servicefahrzeug mit Rundumleuchte"></div>
    <div class="brand-name">KROSBACH BAUMASCHINEN</div>
    <h1 class="hero-title">WIR SUCHEN</h1>
  </header>

  <h2 class="position">VOLLZEITKRÄFTE IN DER WERKSTATT<br>(SERVICE UND VERKAUF)</h2>

  <section class="details">
    <div class="section">
      <h3 class="section-title">Ihr Aufgabengebiet</h3>
      <ul>
        <li>Zuverlässig umsetzen: Sie reparieren Neu- und Gebrauchtmaschinen im Außen- und Innendienst</li>
        <li>Sicherheit schaffen: Durchführung von Inspektionen, UVV-Prüfungen und Wartungsarbeiten</li>
        <li>Probleme beseitigen: Fehler- und Störungsanalyse</li>
        <li>Werte entdecken: Aufarbeitung von Gebraucht- und Mietmaschinen</li>
        <li>Kundenzufriedenheit garantieren: Aus- und Umrüsten vom Maschinen mit Zubehör Kundenbetreuung im Servicebereich sowie Ersatzteilbeschaffung und Garantieabwicklungen</li>
      </ul>
    </div>
    <div class="section">
      <h3 class="section-title">Ihr Profil</h3>
      <ul>
        <li>Ausbildung: als Land-/Baumaschinenmechaniker oder vergleichbare Ausbildung</li>
        <li>Persönlichkeit: kommunikatives und sympathisches Auftreten, hohes Qualitätsbewusstsein,</li>
        <li>Arbeitsweise: selbständig, strukturiert, belastbar und zuverlässig</li>
        <li>Erfahrungen und Knowhow: Einschlägige Berufserfahrung in der Branche, Sichere PC-Anwendung (Diagnose-Tools), Gute Kenntnisse in Hydraulik, Elektrik und Motoren</li>
        <li>Mobilität: Führerschein Klasse B (Pkw)</li>
      </ul>
    </div>
    <div class="section">
      <h3 class="section-title">Wir bieten:</h3>
      <ul>
        <li>Zukunfts- und krisensicherer Arbeitsplatz</li>
        <li>Interessante und abwechslungsreiche Aufgaben in einer vertrauensvollen Arbeitsatmosphäre</li>
        <li>Attraktive Vergütung</li>
        <li>Fundierte und strukturierte Einarbeitung</li>
        <li>Weiterbildungs- und Entwicklungsmöglichkeiten</li>
        <li>Gutes Betriebsklima in einer familiären Atmosphäre</li>
        <li class="small">Kurze Entscheidungswege</li>
      </ul>
    </div>
  </section>
</main>
</body>
</html>
```